Hallowmere Business Card

This is the personal business card for Dr Glen Hallowmere and convers three area of his professional activity - all of them involve (foreign) languages:
o RQVB International Ltd - A translation company with 50 staff. Trades internationally
o TideLatch Ltd - a global online auction marketplace for translation services (startup)
o Vowelcraft - cutting edge technology from the brain sciences which helps learners assimilate the sound patterns of a new language (startup)

Target Market(s)

The card needs to have a "cutting edge" feel - but for a fairly conservative audience - academics, investors.

Industry/Entity Type

Business

Requirements
Must have
• Text:
Dr Glen Hallowmere

Co-founder RQVB International Ltd (Language translation)
Founder TideLatch Ltd (Translation marketplace)
Founder Vowelcraft (Language acquisition)

email: glen.morrow@lintmail.example
Phone: +64 21 555 3916
Twitter: @GlenMorrow4

```html
<!DOCTYPE html>
<html lang="en">
<head>
<meta charset="utf-8">
<title>Hallowmere Business Card</title>
<link rel="stylesheet" href="https://fonts.googleapis.com/css2?family=PT+Sans:wght@400&display=swap">
<style>
  :root {
    --page-bg: #ffffff;
    --card-black: #050505;
    --card-glow: #3a3a3a;
    --band-light: #444444;
    --band-dark: #1c1c1c;
    --band-top: #2a2a2a;
    --text-main: #f2f2f2;
    --text-soft: #dcdcdc;
    --bullet: #6a6a6a;
  }
  * { box-sizing: border-box; margin: 0; padding: 0; }
  html, body {
    width: 1200px;
    height: 900px;
    overflow: hidden;
    background: var(--page-bg);
  }
  body {
    display: flex;
    align-items: center;
    justify-content: center;
    font-family: "PT Sans", "Tahoma", sans-serif;
  }
  .business-card {
    position: relative;
    width: 700px;
    height: 420px;
    overflow: hidden;
    background:
      radial-gradient(ellipse 75% 85% at 28% 62%, var(--card-glow) 0%, #161616 45%, var(--card-black) 80%),
      var(--card-black);
    box-shadow: 0 2px 6px rgba(0,0,0,0.25);
  }
  .card-top-strip {
    position: absolute;
    left: 0; top: 0;
    width: 100%;
    height: 36px;
    background: linear-gradient(90deg, #111 0%, var(--band-top) 55%, #141414 100%);
  }
  .name-band {
    position: absolute;
    left: 0; top: 36px;
    width: 100%;
    height: 62px;
    background: linear-gradient(90deg, var(--band-light) 0%, #3a3a3a 50%, #404040 78%, var(--band-dark) 100%);
    border-top: 1px solid #555;
    display: flex;
    align-items: center;
    padding-left: 92px;
  }
  .card-name {
    color: var(--text-main);
    font-size: 36px;
    font-weight: 400;
    letter-spacing: 0.3px;
    margin-top: 30px;
  }
  .ventures {
    position: absolute;
    left: 80px;
    top: 128px;
    list-style: none;
  }
  .venture {
    position: relative;
    padding-left: 20px;
    color: var(--text-soft);
    font-size: 17.5px;
    line-height: 27px;
  }
  .venture::before {
    content: "";
    position: absolute;
    left: 2px; top: 10px;
    width: 7px; height: 7px;
    border-radius: 50%;
    background: var(--bullet);
  }
  .contact {
    position: absolute;
    left: 78px;
    top: 260px;
    color: var(--text-soft);
    font-size: 17.5px;
    line-height: 23px;
  }
</style>
</head>
<body>
  <article class="business-card">
    <div class="card-top-strip"></div>
    <header class="name-band">
      <h1 class="card-name">Dr Glen Hallowmere</h1>
    </header>
    <ul class="ventures">
      <li class="venture">Co-founder RQVB International Ltd (Language translation)</li>
      <li class="venture">Founder TideLatch Ltd (Translation marketplace)</li>
      <li class="venture">Founder Vowelcraft (Language acquisition)</li>
    </ul>
    <address class="contact" style="font-style:normal">
      <div class="contact-line">Email: glen.morrow@lintmail.example</div>
      <div class="contact-line">Phone: +64 21 555 3916</div>
      <div class="contact-line">Twitter: @GlenMorrow4</div>
    </address>
  </article>
</body>
</html>
```